Business Card Design Project

I have a newly designed logo (by Marlo through Pixel Harbor) and now need a business card concept / design.

We are an HR consulting firm.

I am hoping that someone can advise me if they are able to see the logo that I chose in my last project (logo design) or if I need to upload that logo here in this project?

Obviously I want the business card to fit with the logo!

Industry/Entity Type

Business

```html
<!DOCTYPE html>
<html lang="en">
<head>
<meta charset="utf-8">
<title>Harlow Consulting – Business Cards</title>
<link href="https://fonts.googleapis.com/css2?family=Questrial&display=swap" rel="stylesheet">
<style>
  :root {
    --bg: #e4e6e8;
    --green: #7cc242;
    --green-dark: #5aa02c;
    --blue: #1aa7d6;
    --teal: #2b9fb3;
    --ink: #1c2a30;
    --black: #0d0f10;
    --white: #ffffff;
  }
  html, body {
    margin: 0;
    width: 857px;
    height: 1200px;
    overflow: hidden;
    background: var(--bg);
    font-family: "Questrial", "Century Gothic", sans-serif;
  }
  .canvas {
    position: relative;
    width: 857px;
    height: 1200px;
  }
  .card {
    position: absolute;
    left: 88px;
    width: 680px;
    height: 390px;
    box-sizing: border-box;
    border-radius: 70px 16px 70px 16px;
  }
  .card-front {
    top: 140px;
    background: var(--white);
    border: 16px solid var(--green);
  }
  .card-back {
    top: 670px;
    background: var(--black);
    border: 16px solid var(--blue);
    overflow: hidden;
  }
  .brand {
    position: absolute;
    display: flex;
    align-items: center;
    gap: 12px;
  }
  .brand-dot {
    width: 34px;
    height: 34px;
    border-radius: 50%;
    background: var(--green);
  }
  .brand-name {
    font-size: 40px;
    color: var(--teal);
    letter-spacing: -0.5px;
  }
  .front-brand { left: 40px; top: 34px; }
  .tagline {
    position: absolute;
    left: 86px;
    top: 88px;
    font-size: 14px;
    color: var(--teal);
    letter-spacing: 0.3px;
  }
  .divider {
    position: absolute;
    left: 0;
    top: 100px;
    width: 648px;
    height: 40px;
  }
  .web {
    position: absolute;
    right: 34px;
    top: 142px;
    font-size: 24px;
    color: var(--green-dark);
  }
  .contact {
    position: absolute;
    bottom: 48px;
    font-size: 26px;
    color: var(--teal);
  }
  .contact small {
    display: block;
    font-size: 22px;
    color: var(--green-dark);
    margin-top: 6px;
  }
  .contact-email { left: 46px; }
  .contact-email small { text-align: right; }
  .contact-name { right: 40px; text-align: right; }
  .swoosh {
    position: absolute;
    inset: 0;
    width: 648px;
    height: 358px;
  }
  .back-brand { right: 40px; top: 68px; }
  .back-brand .brand-dot { width: 22px; height: 22px; }
  .back-brand .brand-name { font-size: 26px; color: var(--blue); }
  .back-tagline {
    position: absolute;
    right: 40px;
    top: 104px;
    font-size: 9px;
    color: var(--blue);
  }
  .faint-mark {
    position: absolute;
    left: 60px;
    top: 170px;
    width: 130px;
    height: 130px;
    border-radius: 50%;
    border: 10px solid #2a2d2f;
  }
</style>
</head>
<body>
<main class="canvas">
  <section class="card card-front" aria-label="Business card front">
    <div class="brand front-brand">
      <span class="brand-dot"></span>
      <span class="brand-name">Harlow Consulting</span>
    </div>
    <div class="tagline">Human Resources and Recruitment Solutions</div>
    <svg class="divider" viewBox="0 0 648 40" aria-hidden="true">
      <path d="M40 30 C 200 22, 420 26, 610 30" stroke="#1aa7d6" stroke-width="2" fill="none"/>
    </svg>
    <div class="web">www.harlowconsulting.com</div>
    <div class="contact contact-email">nadia@harlowconsulting.com<small>e-mail</small></div>
    <div class="contact contact-name">Nadia Harlow<small>Director</small></div>
  </section>

  <section class="card card-back" aria-label="Business card back">
    <svg class="swoosh" viewBox="0 0 648 358" aria-hidden="true">
      <path d="M0 60 C 180 70, 300 150, 360 230 C 400 290, 520 300, 648 290"
            stroke="#7cc242" stroke-width="3" fill="none"/>
    </svg>
    <div class="faint-mark"></div>
    <div class="brand back-brand">
      <span class="brand-dot"></span>
      <span class="brand-name">Harlow Consulting</span>
    </div>
    <div class="back-tagline">Human Resources and Recruitment Solutions</div>
  </section>
</main>
</body>
</html>
```